Core Values Poster for Healthcare company

Trying to Create a core values poster for my company. Healthcare Company - We have Neurosurgery, Pain Management, Physical Therapy, Occupational Therapy, Rehab, Imaging, and psychology so far and we are growing fast.

Core Values would Include - (Execution), (Loyalty), (Innovation), (Synergy), (Growth-Oriented), (Ethics & Integrity), (Love), and (Energy)

Please incorporate the Company Logo which is on the website and I have included it in my uploads. As long as the logo stays blue it does not need a gradient effect.

I like the posters made for this contest : https://pinlarkstudio.com.au/flyer-work/briefs/build-team-ideals-flyer-580316

This picture should be memorable so people know our Core Values

Target Market(s)

Staff in the company

Colors

Designer to choose colors to be used in the design.

Requirements
Must have
• Logo
Nice to have
• Pictures for each core value

```html
<!DOCTYPE html>
<html lang="en">
<head>
<meta charset="utf-8">
<title>Core Values – Halcyon</title>
<link href="https://fonts.googleapis.com/css2?family=Oswald:wght@600&family=Poppins:wght@500;600&display=swap" rel="stylesheet">
<style>
  :root{
    --bg-light:#f2f2f2;
    --bg-mid:#d9dadb;
    --navy:#1c4558;
    --deep-teal:#1f5266;
    --teal:#2aa9c2;
    --teal-dark:#1d8aa3;
    --sky:#4fc3d3;
    --red-orange:#e9512b;
    --red:#c3352a;
    --grey:#a3a3a3;
    --grey-dark:#858585;
    --orange:#f7a21b;
    --green:#7fbf3e;
    --green-dark:#3f8a3a;
    --brand-blue:#2a8cc8;
    --white:#ffffff;
  }
  html,body{margin:0;padding:0;overflow:hidden;}
  body{width:848px;height:1200px;}
  .poster{
    position:relative;width:848px;height:1200px;overflow:hidden;
    background:radial-gradient(ellipse at 50% 45%,var(--bg-light) 0%,var(--bg-mid) 100%);
    font-family:"Poppins",sans-serif;
  }
  .backdrop{position:absolute;inset:0;}
  .title{
    position:absolute;right:60px;top:82px;margin:0;
    font-family:"Poppins",sans-serif;font-weight:600;font-size:54px;letter-spacing:2px;
    color:var(--white);text-shadow:2px 3px 4px rgba(0,0,0,.35);line-height:1;
  }
  .value-grid{position:absolute;left:34px;top:220px;filter:drop-shadow(4px 6px 8px rgba(0,0,0,.25));}
  .num{font-family:"Oswald",sans-serif;font-weight:600;font-size:64px;fill:var(--white);text-anchor:middle;}
  .label{font-family:"Poppins",sans-serif;font-weight:600;font-size:27px;fill:var(--white);text-anchor:middle;letter-spacing:1px;}
  .label-side{font-size:28px;}
  .icon{fill:none;stroke:var(--white);stroke-width:7;stroke-linecap:round;stroke-linejoin:round;}
  .centre-name{font-family:"Poppins",sans-serif;font-weight:600;font-size:38px;fill:var(--brand-blue);text-anchor:middle;}
  .brand{position:absolute;left:210px;top:1012px;display:flex;align-items:center;gap:14px;}
  .brand-mark{width:80px;height:80px;background:var(--brand-blue);}
  .brand-name{font-family:"Poppins",sans-serif;font-weight:500;font-size:74px;line-height:1;color:var(--brand-blue);letter-spacing:4px;}
</style>
</head>
<body>
<main class="poster">
  <svg class="backdrop" width="848" height="1200" viewBox="0 0 848 1200" aria-hidden="true">
    <polygon points="0,0 350,0 355,104 0,104" fill="var(--sky)"/>
    <polygon points="0,118 290,118 0,760" fill="var(--navy)"/>
    <polygon points="320,0 848,0 848,162 384,162" fill="var(--deep-teal)"/>
    <polygon points="0,1116 848,1116 848,1200 0,1200" fill="var(--navy)"/>
    <polygon points="470,1200 560,1116 640,1116 760,1200" fill="var(--teal)"/>
  </svg>

  <h1 class="title">CORE VALUES</h1>

  <svg class="value-grid" width="759" height="759" viewBox="0 0 759 759" role="img" aria-label="Eight core values arranged around a centre tile">
    <defs>
      <clipPath id="grid-round"><rect width="759" height="759" rx="26"/></clipPath>
      <linearGradient id="g-red" x1="0" y1="0" x2="1" y2="1"><stop offset="0" stop-color="#e8462a"/><stop offset="1" stop-color="#f06a35"/></linearGradient>
      <linearGradient id="g-grey" x1="0" y1="0" x2="1" y2="1"><stop offset="0" stop-color="#9c9c9c"/><stop offset="1" stop-color="#c4c4c4"/></linearGradient>
      <linearGradient id="g-teal" x1="0" y1="0" x2="1" y2="1"><stop offset="0" stop-color="#2a9fb8"/><stop offset="1" stop-color="#4cc3d2"/></linearGradient>
      <linearGradient id="g-orange" x1="0" y1="0" x2="1" y2="1"><stop offset="0" stop-color="#f28a1c"/><stop offset="1" stop-color="#fbb41e"/></linearGradient>
      <linearGradient id="g-green" x1="0" y1="0" x2="1" y2="1"><stop offset="0" stop-color="#8cc640"/><stop offset="1" stop-color="#3f8a3a"/></linearGradient>
      <linearGradient id="g-navy" x1="0" y1="0" x2="1" y2="1"><stop offset="0" stop-color="#173d50"/><stop offset="1" stop-color="#235a6e"/></linearGradient>
    </defs>
    <g clip-path="url(#grid-round)">
      <!-- tiles -->
      <rect class="tile-execution" x="0" y="0" width="253" height="253" fill="url(#g-red)"/>
      <rect class="tile-loyalty" x="253" y="0" width="253" height="253" fill="url(#g-grey)"/>
      <rect class="tile-innovation" x="506" y="0" width="253" height="253" fill="url(#g-teal)"/>
      <rect class="tile-energy" x="0" y="253" width="253" height="253" fill="url(#g-teal)"/>
      <rect class="tile-centre" x="253" y="253" width="253" height="253" fill="#e4e5e6"/>
      <rect class="tile-synergy" x="506" y="253" width="253" height="253" fill="url(#g-red)"/>
      <rect class="tile-love" x="0" y="506" width="253" height="253" fill="url(#g-orange)"/>
      <rect class="tile-ethics" x="253" y="506" width="253" height="253" fill="url(#g-green)"/>
      <rect class="tile-growth" x="506" y="506" width="253" height="253" fill="url(#g-navy)"/>

      <!-- number tabs -->
      <polygon points="0,253 126,172 253,253" fill="var(--teal-dark)"/>
      <polygon points="253,0 335,127 253,253" fill="var(--red)"/>
      <polygon points="506,0 588,127 506,253" fill="var(--grey-dark)"/>
      <polygon points="506,253 632,335 759,253" fill="var(--teal-dark)"/>
      <polygon points="506,506 632,588 759,506" fill="var(--red)"/>
      <polygon points="506,506 424,632 506,759" fill="var(--deep-teal)"/>
      <polygon points="253,506 171,632 253,759" fill="var(--green-dark)"/>
      <polygon points="0,506 126,425 253,506" fill="var(--orange)"/>
    </g>

    <text class="num" x="126" y="244">01</text>
    <text class="num" x="296" y="150">02</text>
    <text class="num" x="545" y="150">03</text>
    <text class="num" x="632" y="315">04</text>
    <text class="num" x="632" y="567">05</text>
    <text class="num" x="468" y="655">06</text>
    <text class="num" x="214" y="655">07</text>
    <text class="num" x="126" y="495">08</text>

    <text class="label label-side" transform="translate(34 128) rotate(-90)">EXECUTION</text>
    <text class="label label-side" transform="translate(494 152) rotate(-90)">LOYALTY</text>
    <text class="label label-side" transform="translate(740 120) rotate(-90)">INNOVATION</text>
    <text class="label" x="126" y="292">ENERGY</text>
    <text class="label" x="632" y="488">SYNERGY</text>
    <text class="label" x="632" y="706">GROWTH-</text>
    <text class="label" x="632" y="744">ORIENTED</text>
    <text class="label" x="386" y="702">ETHICS &amp;</text>
    <text class="label" x="386" y="742">INTEGRITY</text>
    <text class="label" x="138" y="740">LOVE</text>

    <text class="centre-name" x="379" y="393">HALCYON</text>

    <!-- icons -->
    <g class="icon icon-clipboard">
      <rect x="96" y="70" width="64" height="78" rx="3"/>
      <path d="M114 70 v-8 h28 v8"/>
      <path d="M110 104 l14 16 l26 -32"/>
    </g>
    <g class="icon icon-hands">
      <path d="M360 96 h40 l14 -12 h34"/>
      <path d="M360 134 h30 l28 12 l40 -22"/>
      <path d="M398 122 q8 -14 16 0 q8 -14 16 0 l-16 16 z"/>
    </g>
    <g class="icon icon-bulb">
      <path d="M632 140 v-10 q-20 -14 -20 -34 a28 28 0 0 1 56 0 q0 20 -20 34 v10 z"/>
      <path d="M630 154 h20 M634 164 h12"/>
      <path d="M594 94 h-10 M706 94 h-10 M608 64 l-7 -7 M692 64 l7 -7 M650 48 v-10"/>
    </g>
    <g class="icon icon-energy">
      <circle cx="126" cy="358" r="40"/>
      <path d="M132 334 l-18 28 h16 l-8 22 l22 -30 h-16 z" fill="var(--white)"/>
    </g>
    <g class="icon icon-synergy">
      <circle cx="622" cy="400" r="34"/>
      <circle cx="622" cy="366" r="8" fill="var(--white)"/>
      <circle cx="592" cy="418" r="8" fill="var(--white)"/>
      <circle cx="652" cy="418" r="8" fill="var(--white)"/>
    </g>
    <g class="icon icon-growth">
      <path d="M600 666 v-20 M618 666 v-30 M636 666 v-42 M654 666 v-54"/>
      <path d="M592 638 l26 -24 l18 10 l40 -38"/>
      <path d="M660 584 h18 v18"/>
    </g>
    <g class="icon icon-handshake">
      <path d="M310 610 l24 -22 h20 l24 16 l22 -10"/>
      <path d="M334 602 l28 26 q6 6 0 12 q-6 6 -12 0 l-20 -18"/>
      <path d="M318 622 l22 22 M330 614 l22 22"/>
    </g>
    <g class="icon icon-heart">
      <path d="M98 686 l-38 -36 a24 24 0 0 1 38 -30 a24 24 0 0 1 38 30 z"/>
    </g>
  </svg>

  <div class="brand">
    <div class="brand-mark"></div>
    <span class="brand-name">HALCYON</span>
  </div>
</main>
</body>
</html>
```